TRADE SHOW DISPLAY BANNER Design Project

Looking for a designer to use some photos (that i have taken), edit, cut out, and design a banner for a trade show display that i will be using at an expo.

The approx visible size will be: 295cm wide x 230cm high
(please view display size 1 - for sizes, and display size 2 - for display end product)

Industry/Entity Type

Trade

Requirements
Must have
• - main focus is the steel fence post. will require a picture of the fence with the posts,
photos for this point are ( fence2, fence 3, fence 4, fence 5, fence1 original, fence1)

- the 3 pictures, outlining how the brackets work. on the side
photos for this point are (steel post 1, steel post 2, steel post 3)

Will require 'STEEL FENCE POST' written somewhere on top in large letters. will also require the website written somewhere on the add - 'www.RailvoxUprights.com.au'

Will requite the Dorvell Timber logo somewhere on the bottom corners of the add.
photo of this add is - 'dorvell timber logo'

the exact dimensions of the add can be seen in 'display size1'
the end product of the add will look like 'display size2'

```html
<!DOCTYPE html>
<html lang="en">
<head>
<meta charset="utf-8">
<title>Steel Fence Post – Trade Show Banner</title>
<link rel="stylesheet" href="https://fonts.googleapis.com/css2?family=Roboto+Condensed:wght@400;500&family=Open+Sans:wght@400&display=swap">
<style>
  :root {
    --navy-deep: #062a4f;
    --navy: #0b4072;
    --navy-mid: #0e4d86;
    --sky: #2aa8e2;
    --sky-soft: #3fb4e8;
    --white: #ffffff;
    --frame: #5cc6f2;
    --photo-wood: #b59b77;
    --photo-wood-dark: #8c7554;
    --photo-steel: #a9adb0;
    --photo-sky: #cfd9e2;
  }
  html, body {
    margin: 0;
    padding: 0;
    width: 1200px;
    height: 960px;
    overflow: hidden;
    background: #1a1a1a;
  }
  .banner {
    position: relative;
    width: 1200px;
    height: 960px;
    overflow: hidden;
    background: linear-gradient(180deg, var(--navy) 0%, var(--navy-mid) 30%, var(--navy) 60%, var(--navy-deep) 100%);
    font-family: "Roboto Condensed", "Arial Narrow", sans-serif;
  }
  .banner__waves {
    position: absolute;
    inset: 0;
  }
  .banner__title {
    position: absolute;
    left: 56px;
    top: 38px;
    margin: 0;
    font-weight: 400;
    font-size: 118px;
    line-height: 1;
    letter-spacing: -1px;
    color: var(--white);
    text-shadow: 5px 6px 6px rgba(0, 0, 0, 0.75);
    white-space: nowrap;
  }
  .gallery {
    position: absolute;
    top: 219px;
    left: 56px;
    display: flex;
    gap: 27px;
  }
  .gallery__photo {
    width: 243px;
    height: 350px;
    border: 2px solid var(--frame);
    border-radius: 3px;
    box-shadow: 0 0 8px rgba(0, 0, 0, 0.4);
  }
  .gallery__photo--corner { background: linear-gradient(180deg, #6d5f55 0%, var(--photo-wood) 15%, var(--photo-wood-dark) 100%); }
  .gallery__photo--run { background: linear-gradient(180deg, var(--photo-sky) 0%, #a89c8b 25%, var(--photo-wood) 55%, #7a6a52 100%); }
  .gallery__photo--bracket { background: linear-gradient(180deg, var(--photo-steel) 0%, #c4c7c9 35%, #c9bda6 55%, #8f9295 100%); }
  .gallery__photo--side { background: linear-gradient(90deg, #9a8a74 0%, #a99374 55%, #7d6a52 100%); }
  .banner__tagline {
    position: absolute;
    left: 56px;
    top: 622px;
    margin: 0;
    font-weight: 400;
    font-size: 92px;
    line-height: 1;
    letter-spacing: -1px;
    color: var(--sky);
    text-shadow: 4px 5px 6px rgba(0, 0, 0, 0.7);
    white-space: nowrap;
  }
  .banner__subline {
    position: absolute;
    left: 56px;
    top: 718px;
    margin: 0;
    font-weight: 400;
    font-size: 70px;
    line-height: 1;
    color: var(--white);
    text-shadow: 3px 4px 5px rgba(0, 0, 0, 0.6);
    white-space: nowrap;
    word-spacing: 6px;
  }
  .banner__web {
    position: absolute;
    left: 43px;
    top: 878px;
    font-family: "Open Sans", Arial, sans-serif;
    font-size: 42px;
    color: var(--white);
    white-space: nowrap;
  }
  .brand {
    position: absolute;
    right: 42px;
    top: 852px;
    display: flex;
    align-items: center;
    gap: 14px;
    font-weight: 500;
    font-size: 52px;
    color: var(--white);
    white-space: nowrap;
  }
  .brand__mark {
    width: 22px;
    height: 22px;
    background: var(--white);
  }
</style>
</head>
<body>
<main class="banner">
  <svg class="banner__waves" width="1200" height="960" viewBox="0 0 1200 960" aria-hidden="true">
    <path d="M0 190 C 150 120, 300 160, 420 260 S 760 520, 1200 480 L1200 520 C 760 560, 420 360, 300 260 S 120 160, 0 230 Z" fill="#0a3a68" opacity="0.7"/>
    <path d="M0 170 C 140 120, 300 140, 400 250" fill="none" stroke="var(--sky)" stroke-width="5" opacity="0.75"/>
    <path d="M1200 200 C 1120 260, 1080 300, 1040 330" fill="none" stroke="#1f72c4" stroke-width="10" opacity="0.8"/>
    <path d="M1200 270 C 1160 330, 1100 400, 1060 420" fill="none" stroke="#1c64b0" stroke-width="6" opacity="0.7"/>
    <path d="M1200 360 C 1160 390, 1120 410, 1070 425" fill="none" stroke="#2a86d6" stroke-width="5" opacity="0.7"/>
    <path d="M0 300 C 40 320, 60 330, 90 350" fill="none" stroke="#0c2f56" stroke-width="12" opacity="0.8"/>
    <path d="M500 700 C 750 730, 1000 780, 1200 830" fill="none" stroke="#0d4a85" stroke-width="26" opacity="0.6"/>
    <path d="M700 960 C 680 880, 720 830, 820 815 C 950 800, 1100 820, 1200 860 L1200 960 Z" fill="var(--sky)"/>
  </svg>

  <h1 class="banner__title">STEEL FENCE POST</h1>

  <div class="gallery">
    <div class="gallery__photo gallery__photo--corner" role="img" aria-label="Photo of a timber paling fence corner fixed to a steel fence post"></div>
    <div class="gallery__photo gallery__photo--run" role="img" aria-label="Photo of a long timber paling fence run supported by steel posts beside a house"></div>
    <div class="gallery__photo gallery__photo--bracket" role="img" aria-label="Close-up photo of a galvanised bracket bolting a timber rail to a steel post"></div>
    <div class="gallery__photo gallery__photo--side" role="img" aria-label="Photo of a finished timber fence with steel posts seen from the side"></div>
  </div>

  <p class="banner__tagline">Slim, Lightweight &amp; Durable</p>
  <p class="banner__subline">The Timber Alternative</p>

  <div class="banner__web">www.RailvoxUprights.com.au</div>

  <div class="brand">
    <span class="brand__mark"></span>
    <span class="brand__name">Dorvell Timber</span>
  </div>
</main>
</body>
</html>
```